Vantor Ridge needs a Business Card Design

We need a business card design for an Information Technology company based in Fairfax Virginia called Vantor Ridge. We want the business card to use our logo colors. We need it to be double-sided. The business card needs to look professional but we would like it to be unique. You can get company information from our web site (http://www.vantorridgellc.example).

Target Market(s)

Target market is Government Agencies and Business Professionals.

Industry/Entity Type

Business

Requirements
Must have
• Must have section for company name, company address, company URL, employee name, title, phone and email. Also must have company logo and space for entering logos.

```html
<!DOCTYPE html>
<html lang="en">
<head>
<meta charset="utf-8">
<title>Vantor Ridge – Business Card</title>
<link rel="stylesheet" href="https://fonts.googleapis.com/css2?family=Open+Sans:wght@400;600;700;800&display=swap">
<style>
  :root {
    --navy: #23339a;
    --royal: #2a3fae;
    --sky: #1a7fc8;
    --ink: #3a3f52;
    --muted: #5a6070;
    --paper: #ffffff;
    --backdrop: #e9e6e0;
  }
  * { box-sizing: border-box; margin: 0; padding: 0; }
  html, body { width: 1200px; height: 1024px; overflow: hidden; }
  body {
    background: var(--backdrop);
    font-family: "Open Sans", Arial, sans-serif;
    position: relative;
  }
  .card {
    position: absolute;
    left: 250px;
    width: 700px;
    height: 400px;
    border-radius: 4px;
    overflow: hidden;
    box-shadow: 0 10px 28px rgba(40, 35, 25, 0.25);
  }
  /* Front */
  .card-front { top: 72px; background: var(--paper); }
  .front-band {
    position: absolute; left: 0; right: 0; bottom: 0; height: 40px;
    background: var(--navy);
  }
  .front-band-accent {
    position: absolute; right: 0; bottom: 40px; width: 150px; height: 16px;
    background: var(--sky);
  }
  .brand {
    position: absolute; left: 56px; top: 96px;
    display: flex; align-items: center; gap: 14px;
  }
  .brand-square { width: 40px; height: 40px; background: var(--royal); }
  .brand-name {
    font-weight: 800; font-size: 34px; line-height: 1;
    color: var(--royal); letter-spacing: 0.5px; text-transform: uppercase;
    white-space: nowrap;
  }
  .brand-tagline {
    position: absolute; left: 110px; top: 140px;
    font-size: 10px; font-weight: 600; letter-spacing: 0.6px;
    color: var(--ink); text-transform: uppercase; white-space: nowrap;
  }
  .divider {
    position: absolute; left: 432px; top: 92px; width: 1px; height: 150px;
    background: linear-gradient(var(--paper), var(--navy), var(--paper));
  }
  .contact-list {
    position: absolute; left: 455px; top: 112px; list-style: none;
    font-size: 14px; color: var(--ink);
  }
  .contact-list li { display: flex; align-items: center; gap: 10px; height: 27px; white-space: nowrap; }
  .contact-list svg { width: 13px; height: 13px; fill: var(--royal); flex: none; }
  .person {
    position: absolute; left: 56px; top: 262px;
  }
  .person-name { font-size: 17px; font-weight: 700; color: var(--navy); }
  .person-title { font-size: 15px; color: var(--sky); margin-bottom: 4px; }
  .address { display: flex; gap: 8px; font-size: 15px; color: var(--muted); line-height: 1.35; }
  .address svg { width: 13px; height: 13px; fill: var(--royal); margin-top: 3px; flex: none; }

  /* Back */
  .card-back {
    top: 552px;
    background: linear-gradient(135deg, var(--royal) 0%, var(--navy) 100%);
  }
  .back-band {
    position: absolute; left: 0; right: 0; top: 150px; height: 90px;
    background: var(--sky);
  }
  .back-brand {
    position: absolute; left: 56px; top: 272px;
    display: flex; align-items: center; gap: 12px;
  }
  .back-brand .brand-square { width: 32px; height: 32px; background: var(--paper); }
  .back-brand .brand-name { font-size: 30px; color: var(--paper); }
  .back-tagline {
    position: absolute; left: 100px; top: 310px;
    font-size: 9.5px; font-weight: 600; letter-spacing: 0.6px;
    color: var(--paper); text-transform: uppercase; white-space: nowrap;
  }
  .back-url {
    position: absolute; right: 30px; top: 24px;
    font-size: 12px; color: rgba(255,255,255,0.8);
  }
</style>
</head>
<body>

<section class="card card-front" aria-label="Business card front">
  <div class="brand">
    <span class="brand-square"></span>
    <span class="brand-name">Vantor Ridge</span>
  </div>
  <p class="brand-tagline">Reliable technology for every mission</p>

  <div class="divider"></div>

  <ul class="contact-list">
    <li><svg viewBox="0 0 16 16"><path d="M3.5 1l3 3-1.6 1.8a9 9 0 0 0 5.3 5.3L12 9.5l3 3-2 2.3C6.8 14.5 1.5 9.2 1.2 3z"/></svg>877.555.0142</li>
    <li><svg viewBox="0 0 16 16"><path d="M4 0h8v16H4zM5.5 2v10h5V2zM7.2 13.2h1.6v1.4H7.2z"/></svg>888.555.0187</li>
    <li><svg viewBox="0 0 16 16"><path d="M1 3h14v10H1zM2.5 4.5v.4L8 9l5.5-4.1v-.4z"/></svg>name@vantorridge.example</li>
    <li><svg viewBox="0 0 16 16"><path d="M8 1a7 7 0 1 0 0 14A7 7 0 0 0 8 1zm0 1.5c.8 0 1.7 1.6 2 4H6c.3-2.4 1.2-4 2-4zM6 8h4c-.2 3-1.2 5.5-2 5.5S6.2 11 6 8zM2.6 8h2c0 2 .4 3.7 1 4.8A5.5 5.5 0 0 1 2.6 8zm8.8 0h2a5.5 5.5 0 0 1-3 4.8c.6-1.1 1-2.8 1-4.8zM2.7 6.5a5.5 5.5 0 0 1 2.9-3.8c-.5 1-.9 2.3-1 3.8zm8.7 0c-.1-1.5-.5-2.8-1-3.8a5.5 5.5 0 0 1 2.9 3.8z"/></svg>www.vantorridgellc.example</li>
  </ul>

  <div class="person">
    <p class="person-name">Daniel Morrow</p>
    <p class="person-title">Job Title</p>
    <div class="address">
      <svg viewBox="0 0 16 16"><path d="M8 1L1 8h2v7h4v-4h2v4h4V8h2z"/></svg>
      <p>4150 Linden Park Dr, Suite 300<br>Fairfax, VA 22030</p>
    </div>
  </div>

  <div class="front-band-accent"></div>
  <div class="front-band"></div>
</section>

<section class="card card-back" aria-label="Business card back">
  <p class="back-url">www.vantorridgellc.example</p>
  <div class="back-band"></div>
  <div class="back-brand">
    <span class="brand-square"></span>
    <span class="brand-name">Vantor Ridge</span>
  </div>
  <p class="back-tagline">Reliable technology for every mission</p>
</section>

</body>
</html>
```